Consulting company, design, Interior design in commercial real estate (Tertiai sector *

Company name: VORANDEL: from the Greek Evexia well-being, was born from a desire to combine well-being and work. By the choice of design, materials, design and furniture, everything is thought from this perspective

Logo: Essay with Möbius Ribbon and / or with the infinite acronym / and or triangle ...
Sentences to write:
"The exclusive partner for your development projects"
"Consulting - Design - Construction"
"We manage EVERYTHING for you"

On the back: Photo (attached; if photo is not clear, another photo can be provided) with company name and "VORANDEL, Excellence and reliability"
My name / First name: provided later (double name), Manager
Address: supplied later
Tel: supplied later
Website: www. vorandel.com
Colors: Black, gold and white. Other admissible colors
See attached files

Real estate business

Nom de l'entreprise : VORANDEL : du grec Evexia bien être, est né d'une volonté de faire rimer bien être et travail. Par le choix de la conception, des matériaux, du design et du mobilier, tout est pensé dans cette optique

Logo : Essai avec Ruban de Möbius et /ou avec le sigle infini / et ou triangle...
Phrases à inscrire :
"Le partenaire exclusif de vos projets d'aménagement"
"Conseil - Conception - Construction"
"Nous gérons TOUT pour vous"

Au verso : Photo (ci-jointe ; si photo pas nette, une autre photo peut être fournie) avec nom de l'entreprise et Mention "VORANDEL, Excellence et fiabilité"
Mon nom / Prénom : fourni ultérieurement (prénom double), Gérant
Adresse : fourni ultérieurement
Tél : fourni ultérieurement
Site Web : www. vorandel.com
Couleurs : Noir, doré et blanc. Autre couleurs recevables
Voir fichiers ci-joint

• My project must be simple, clear, neat and design.
The business card must catch the customer

```html
<!DOCTYPE html>
<html lang="en">
<head>
<meta charset="utf-8">
<title>VORANDEL — Business Card</title>
<link rel="stylesheet" href="https://fonts.googleapis.com/css2?family=Montserrat:wght@300;400;500;700&display=swap">
<style>
  :root {
    --backdrop: #2c2d2a;
    --card: #111111;
    --card-edge: #1c1c1c;
    --gold: #d4a93e;
    --gold-soft: #b8902f;
    --white: #ffffff;
    --muted: #e6e6e6;
    --photo-dark: #151515;
    --photo-mid: #4a4643;
  }
  * { box-sizing: border-box; margin: 0; padding: 0; }
  html, body {
    width: 1200px; height: 824px; overflow: hidden;
    background: var(--backdrop);
    font-family: "Montserrat", sans-serif;
    color: var(--white);
  }
  .canvas { position: relative; width: 1200px; height: 824px; }

  .card {
    position: absolute;
    width: 520px; height: 300px;
    background: var(--card);
    border: 1px solid var(--card-edge);
    border-radius: 4px;
    box-shadow: 0 10px 30px rgba(0,0,0,.45);
    overflow: hidden;
  }

  /* Front */
  .card-front { left: 50px; top: 120px; display: flex; flex-direction: column; align-items: center; justify-content: center; }
  .brand-dot { width: 62px; height: 62px; border-radius: 50%; background: var(--gold); margin-bottom: 18px; }
  .brand-name { font-weight: 400; font-size: 40px; letter-spacing: 12px; padding-left: 12px; color: var(--white); }
  .brand-services { margin-top: 8px; font-size: 12px; letter-spacing: 2px; color: var(--gold); font-weight: 400; }
  .brand-services .sep { color: var(--white); padding: 0 8px; }
  .brand-tagline { margin-top: 14px; font-size: 12px; color: var(--muted); font-weight: 400; }
  .brand-tagline strong { font-weight: 700; color: var(--white); }

  /* Back */
  .card-back { left: 630px; top: 120px; }
  .holder { position: absolute; left: 34px; top: 32px; }
  .holder-name { font-size: 22px; font-weight: 500; letter-spacing: 1.5px; }
  .holder-role { margin-top: 4px; font-size: 11px; font-weight: 700; letter-spacing: 1px; color: var(--gold); }
  .contact { position: absolute; left: 34px; top: 130px; list-style: none; font-size: 12.5px; font-weight: 400; color: var(--muted); }
  .contact li { display: flex; align-items: center; gap: 8px; margin-bottom: 9px; line-height: 1.25; }
  .contact .address { padding-left: 22px; margin-bottom: 12px; }
  .contact svg { width: 14px; height: 14px; flex: none; }
  .portrait {
    position: absolute; right: 40px; bottom: 0;
    width: 210px; height: 210px;
    background: linear-gradient(180deg, var(--photo-mid) 0%, var(--photo-dark) 100%);
    border-radius: 105px 105px 0 0;
  }

  /* Lockup */
  .lockup { position: absolute; left: 64px; top: 560px; display: flex; flex-direction: column; align-items: center; width: 380px; }
  .lockup .brand-dot { width: 110px; height: 110px; margin-bottom: 30px; }
  .lockup .brand-name { font-size: 50px; letter-spacing: 14px; padding-left: 14px; font-weight: 300; }
</style>
</head>
<body>
<main class="canvas">

  <section class="card card-front" aria-label="Card front">
    <div class="brand-dot"></div>
    <h1 class="brand-name">VORANDEL</h1>
    <p class="brand-services">CONSULTING<span class="sep">|</span>DESIGN<span class="sep">|</span>CONSTRUCTION</p>
    <p class="brand-tagline">We manage <strong>EVERYTHING</strong> for you</p>
  </section>

  <section class="card card-back" aria-label="Card back">
    <div class="holder">
      <h2 class="holder-name">YOUR NAME</h2>
      <p class="holder-role">MANAGER</p>
    </div>
    <ul class="contact">
      <li class="address">000 Anywhere<br>City, ST 00000</li>
      <li>
        <svg viewBox="0 0 24 24" fill="var(--gold)"><path d="M6.6 10.8a15.1 15.1 0 0 0 6.6 6.6l2.2-2.2c.3-.3.7-.4 1-.2 1.1.4 2.3.6 3.6.6.6 0 1 .4 1 1V20c0 .6-.4 1-1 1A17 17 0 0 1 3 4c0-.6.4-1 1-1h3.5c.6 0 1 .4 1 1 0 1.3.2 2.5.6 3.6.1.3 0 .7-.2 1l-2.3 2.2z"/></svg>
        000 000 0000
      </li>
      <li>
        <svg viewBox="0 0 24 24" fill="var(--gold)"><path d="M2 5h20v14H2z" opacity=".0"/><path d="M3 5h18c.6 0 1 .4 1 1v12c0 .6-.4 1-1 1H3c-.6 0-1-.4-1-1V6c0-.6.4-1 1-1zm1 2.2V17h16V7.2l-8 5.3-8-5.3z"/></svg>
        name@vorandel.com
      </li>
      <li>
        <svg viewBox="0 0 24 24" fill="none" stroke="var(--gold)" stroke-width="2"><circle cx="12" cy="12" r="9"/><path d="M3 12h18M12 3c3 3 3 15 0 18M12 3c-3 3-3 15 0 18"/></svg>
        www. vorandel.com
      </li>
    </ul>
    <div class="portrait" role="img" aria-label="Portrait photo of the manager in a dark suit jacket and white shirt"></div>
  </section>

  <div class="lockup">
    <div class="brand-dot"></div>
    <p class="brand-name">VORANDEL</p>
  </div>

</main>
</body>
</html>
```